Engineering group involved with fire safety needs a business card

We need a business card design for a company based in Greece called "Varotis Group". We are engineers and specialized technicians, operating the following : a) Fire fighting equipment trade b) Installation , Inspection & Maintenance of fire extinguishers and fire protection systems c) Occupational Health & Safety (Risk assessment & management/ Staff training). We need a clear and simple card design. I uploaded a draft I made, in order to give you an idea of the company and how I currently imagine the design of the card. I also uploaded the logo in .png file format. We are always open to different, new suggestions and ideas you may want to submit.
Target Market(s)
industries, companies, managers, retail clients
Industry/Entity Type
Fire Safety
Contact Information for Business Card
Addresses & phone numbers (headquarters + branch), logo, name (you can find all the details on the uploaded files!)
Colors
Designer to choose colors to be used in the design.
Look and feel
Each slider illustrates characteristics of the customer's brand and the style your logo design should communicate.

```html
<!DOCTYPE html>
<html lang="en">
<head>
<meta charset="utf-8">
<title>Varotis Group – Business Card</title>
<link rel="stylesheet" href="https://fonts.googleapis.com/css2?family=Lato:wght@400;700&display=swap">
<style>
  :root {
    --page-bg: #d6d6d6;
    --card-bg: #232323;
    --brand-red: #e52d2d;
    --text-light: #ffffff;
    --text-soft: #f2f2f2;
  }
  * { box-sizing: border-box; margin: 0; padding: 0; }
  html, body {
    width: 1000px; height: 1200px; overflow: hidden;
    background: var(--page-bg);
    font-family: "Lato", Arial, sans-serif;
  }
  .card {
    position: absolute;
    background: var(--card-bg);
    box-shadow: 0 10px 22px rgba(0,0,0,0.45);
    overflow: hidden;
  }
  .card-front { left: 111px; top: 120px; width: 777px; height: 446px; }
  .card-back  { left: 109px; top: 633px; width: 781px; height: 446px; }

  .footer-band {
    position: absolute; left: 0; right: 0; bottom: 0; height: 42px;
    background: var(--brand-red);
    color: var(--text-light);
    font-size: 19px;
    display: flex; align-items: center; justify-content: center;
  }

  .brand-name {
    position: absolute;
    display: flex; align-items: center; justify-content: center; gap: 14px;
    color: var(--brand-red);
    font-weight: 700;
    font-size: 42px;
    letter-spacing: 1px;
    text-transform: uppercase;
    white-space: nowrap;
  }
  .brand-mark { width: 22px; height: 22px; background: var(--brand-red); flex: none; }
  .brand-lines { display: flex; flex-direction: column; line-height: 44px; text-align: left; }

  .card-front .brand-name { left: 20px; width: 300px; top: 178px; font-size: 40px; }
  .card-back .brand-name { left: 0; right: 0; top: 116px; }

  .divider {
    position: absolute; left: 340px; top: 136px;
    width: 2px; height: 176px; background: var(--brand-red);
  }

  .contact-block { position: absolute; left: 380px; top: 130px; }
  .person-name {
    color: var(--brand-red); font-weight: 700; font-size: 23px;
    letter-spacing: 0.3px; line-height: 28px;
  }
  .person-role { color: var(--text-soft); font-size: 19px; line-height: 26px; margin-top: 2px; }
  .contact-list { list-style: none; margin-top: 20px; }
  .contact-item {
    display: flex; align-items: center; gap: 10px;
    color: var(--text-soft); font-size: 19px; line-height: 28px;
  }
  .contact-icon { width: 18px; height: 18px; flex: none; }
  .contact-icon * { fill: var(--brand-red); }

  .service-list {
    position: absolute; left: 195px; top: 248px; width: 392px;
    list-style: none; text-align: center;
  }
  .service-item {
    color: var(--text-soft); font-size: 20px; line-height: 34px;
    text-transform: uppercase; position: relative;
  }
  .service-item + .service-item::before {
    content: ""; position: absolute; left: 0; right: 0; top: -1px; height: 2px;
    background: linear-gradient(90deg, transparent, var(--brand-red) 12%, var(--brand-red) 88%, transparent);
  }
</style>
</head>
<body>

<section class="card card-front" aria-label="Business card front">
  <div class="brand-name"><span class="brand-mark"></span><span class="brand-lines"><span>Varotis</span><span>Group</span></span></div>
  <div class="divider"></div>
  <div class="contact-block">
    <p class="person-name">NIKOLAOS VAROTIS</p>
    <p class="person-role">Mechanical Engineer - OHS Consultant</p>
    <ul class="contact-list">
      <li class="contact-item">
        <svg class="contact-icon" viewBox="0 0 24 24"><path d="M12 2a7 7 0 0 0-7 7c0 5 7 13 7 13s7-8 7-13a7 7 0 0 0-7-7zm0 9.5A2.5 2.5 0 1 1 12 6.5a2.5 2.5 0 0 1 0 5z"/></svg>
        K. Palama 12, 19400 Keratea
      </li>
      <li class="contact-item">
        <svg class="contact-icon" viewBox="0 0 24 24"><path d="M6.6 10.8a15.1 15.1 0 0 0 6.6 6.6l2.2-2.2a1 1 0 0 1 1-.25 11.4 11.4 0 0 0 3.6.57 1 1 0 0 1 1 1V20a1 1 0 0 1-1 1A17 17 0 0 1 3 4a1 1 0 0 1 1-1h3.5a1 1 0 0 1 1 1c0 1.25.2 2.45.57 3.57a1 1 0 0 1-.25 1z"/></svg>
        +30 22990 41820
      </li>
      <li class="contact-item">
        <svg class="contact-icon" viewBox="0 0 24 24"><path d="M2 6h20v12H2z M3.5 7.2 12 13l8.5-5.8" /></svg>
        info@varotisgroup.gr
      </li>
      <li class="contact-item">
        <svg class="contact-icon" viewBox="0 0 24 24"><path d="M12 2a10 10 0 1 0 0 20 10 10 0 0 0 0-20zm6.9 6h-2.9a15 15 0 0 0-1.4-3.6A8 8 0 0 1 18.9 8zM12 4c.8 1.2 1.5 2.5 1.9 4h-3.8c.4-1.5 1.1-2.8 1.9-4zM4.3 14a8 8 0 0 1 0-4h3.3a16 16 0 0 0 0 4zm.8 2h2.9c.3 1.300.8 2.500 1.4 3.600A8 8 0 0 1 5.1 16zM8 8H5.1a8 8 0 0 1 4.3-3.6C8.8 5.5 8.3 6.7 8 8zm4 12c-.8-1.2-1.5-2.5-1.9-4h3.8c-.4 1.5-1.1 2.8-1.9 4zm2.3-6H9.7a14 14 0 0 1 0-4h4.6a14 14 0 0 1 0 4zm.3 5.6c.6-1.1 1.1-2.3 1.4-3.6h2.9a8 8 0 0 1-4.3 3.6zM16.4 14a16 16 0 0 0 0-4h3.3a8 8 0 0 1 0 4z"/></svg>
        www.varotisgroup.gr
      </li>
    </ul>
  </div>
  <div class="footer-band">Installation - Inspection - Maintenance</div>
</section>

<section class="card card-back" aria-label="Business card back">
  <div class="brand-name"><span class="brand-mark"></span>Varotis Group</div>
  <ul class="service-list">
    <li class="service-item">Fire Fighting Equipment</li>
    <li class="service-item">Licensing &amp; Business Registration</li>
    <li class="service-item">Occupational Health &amp; Safety</li>
    <li class="service-item">Staff Training</li>
  </ul>
  <div class="footer-band">www.varotisgroup.gr</div>
</section>

</body>
</html>
```